Consultant Firm Marketing Flyer

I want to use this flyer to market health care consultant services. I would like a front and back glossy, professional, yet bold and eye catching design. I would like it to convey knowledge, expertise, partnership and strength. The colors should blue and white but I am very open to the designer being creative. You can visit my website to see colors and images I want to use at brightharborcare.net
I would like the home page image on my website to be incorporated into the flyer but I am also open to other images that work with the design. The designer can be creative.

I want to highlight 4 service area’s of focus to my clients:
1. Revenue Cycle Optimization (making my clients money)
2. Practice Management Optimization (improving clinical operations)
3. Health Compliance (following the law)
4. Health Care Technology: (Telemedicine and AI)
Please be creative. Go where ever your creativity leads.

```html
<!DOCTYPE html>
<html lang="en">
<head>
<meta charset="utf-8">
<title>Bright Harbor Care Partners – Flyer</title>
<link href="https://fonts.googleapis.com/css2?family=Montserrat:wght@300;400;600;700;800&family=Roboto:wght@400;500;700&display=swap" rel="stylesheet">
<style>
:root{
  --blue:#0a4ea3;
  --blue-deep:#083f88;
  --sky:#2a9ad6;
  --sky-light:#5bb8e8;
  --ink:#333a44;
  --grey:#6b6b6b;
  --canvas:#d4d4d4;
  --white:#ffffff;
  --accent:#d9496e;
}
*{margin:0;padding:0;box-sizing:border-box}
html,body{width:1200px;height:3062px;overflow:hidden}
body{background:var(--canvas);font-family:"Roboto",sans-serif;color:var(--ink);position:relative}
.page{position:absolute;left:268px;width:669px;height:952px;background:var(--white);overflow:hidden;box-shadow:6px 6px 10px rgba(0,0,0,.35)}
.page--front{top:990px}
.page--back{top:2016px}
.abs{position:absolute}
.photo{position:absolute}
.section-title{font-family:"Montserrat",sans-serif;font-weight:800;color:var(--sky);font-size:20px;letter-spacing:.3px}
.body-text{font-size:10px;line-height:12px;color:var(--ink)}
.on-blue{color:var(--white)}

/* front */
.hero-photo{left:0;top:0;width:420px;height:360px;background:linear-gradient(90deg,#c9c3bc 0%,#e7e3df 55%,#ffffff 100%)}
.brand{left:380px;top:48px;width:260px;text-align:center}
.brand__mark{display:inline-flex;align-items:center;gap:8px;font-family:"Montserrat",sans-serif;font-weight:800;font-size:38px;color:var(--blue);letter-spacing:2px}
.brand__dot{width:12px;height:12px;border-radius:50%;background:var(--sky)}
.brand__name{font-family:"Montserrat",sans-serif;font-size:11px;font-weight:400;color:var(--ink);letter-spacing:.4px;margin-top:4px}
.headline{left:368px;top:160px;font-family:"Montserrat",sans-serif;line-height:40px;font-size:38px}
.headline__light{font-weight:300;color:var(--sky)}
.headline__bold{font-weight:800;color:var(--blue)}
.headline__o{color:var(--accent)}
.service-panel{left:331px;top:366px;width:338px;height:520px;background:var(--blue);border-top-left-radius:34px}
.about{left:39px;top:380px;width:265px}
.title-rule{width:28px;height:2px;background:var(--sky);margin:4px 0 12px}
.pillars{left:39px;top:650px}
.pillar{display:flex;align-items:center;gap:14px;height:58px}
.pillar__icon{width:46px;height:46px;border-radius:50%;border:2px solid var(--blue);display:flex;align-items:center;justify-content:center}
.pillar__label{font-family:"Montserrat",sans-serif;font-weight:700;font-size:13px;color:var(--sky);line-height:14px}
.services{left:356px;top:378px;width:290px}
.service{position:relative;padding-left:41px;margin-bottom:16px}
.service__icon{position:absolute;left:0;top:0;width:28px;height:28px}
.service__name{font-family:"Roboto",sans-serif;font-size:12px;color:var(--white);font-weight:500}
.service__sub{font-size:10px;font-weight:700;color:var(--white);margin:2px 0 6px}
.service .body-text{font-size:9.2px;line-height:11px;color:#e3ecf7}
.footer{left:0;top:886px;width:669px;height:66px;background:var(--grey);border-top:4px solid var(--sky)}
.call{left:42px;top:20px;font-family:"Montserrat",sans-serif;color:var(--white);display:flex;align-items:baseline;gap:14px}
.call__label{font-weight:700;font-size:13px}
.call__phone{font-weight:700;font-size:24px}
.contact{left:412px;top:11px;color:var(--white);font-size:13px;line-height:21px}
.contact__row{display:flex;align-items:center;gap:8px}

/* back */
.desk-photo{left:0;top:0;width:669px;height:370px;background:linear-gradient(160deg,#3e3a36 0%,#6a5c4c 45%,#b7a48a 70%,#8a8f96 100%)}
.expertise-panel{left:330px;top:346px;width:339px;height:552px;background:var(--blue);border-top-left-radius:34px;overflow:hidden}
.team-photo{left:0;top:382px;width:339px;height:170px;background:linear-gradient(180deg,var(--blue) 0%,#5f7ea6 35%,#cfd6de 100%)}
.left-col{left:43px;top:396px;width:265px}
.left-col .section-title{margin-bottom:8px}
.left-col .body-text{margin-bottom:22px}
.map{left:43px;top:752px;width:240px;height:102px;border-radius:10px;background:linear-gradient(135deg,#e8eef3 0%,#d6e4ee 50%,#eef1e6 100%)}
.expertise{left:30px;top:40px;width:290px}
.expertise__sub{font-size:12px;color:var(--white);margin:1px 0 14px}
.expertise .body-text{color:#e3ecf7;font-size:10px;margin-bottom:14px}
.checks{list-style:none}
.checks li{display:flex;gap:9px;align-items:flex-start;font-size:10px;font-weight:700;color:var(--white);line-height:12px;margin-bottom:11px}
.checks svg{flex:none}
.corner-wave{left:0;top:820px}
.address{left:45px;top:20px;color:var(--white);font-family:"Montserrat",sans-serif;font-weight:700;font-size:14px;display:flex;align-items:center;gap:10px}
.web{left:400px;top:20px;color:var(--white);font-size:13px;display:flex;align-items:center;gap:8px}
</style>
</head>
<body>

<!-- FRONT -->
<section class="page page--front">
  <div class="photo hero-photo" role="img" aria-label="Team of healthcare professionals in a meeting around a table"></div>
  <svg class="abs" style="left:0;top:300px" width="669" height="90" viewBox="0 0 669 90">
    <path d="M0 40 Q0 60 30 60 L669 60 L669 90 L0 90Z" fill="#fff"/>
    <path d="M0 46 Q0 64 30 64 L600 64 Q660 64 669 20 L669 30 Q660 70 600 70 L30 70 Q0 70 0 52Z" fill="var(--sky)"/>
  </svg>
  <div class="abs brand">
    <div class="brand__mark"><span class="brand__dot"></span>BHC</div>
    <div class="brand__name">Bright Harbor Care Partners LLC</div>
  </div>
  <h1 class="abs headline">
    <div class="headline__light">ADVANCING</div>
    <div class="headline__bold">HEALTHCARE</div>
    <div class="headline__bold"><span class="headline__o">O</span>PERATIONAS</div>
  </h1>

  <div class="abs service-panel"></div>

  <div class="abs about">
    <h2 class="section-title">ABOUT US</h2>
    <div class="title-rule"></div>
    <p class="body-text">Bright Harbor Care Partners (BHC), founded in 2015, is a healthcare consulting firm skilled at helping physician practices advance their strategic vision in an ever-evolving healthcare system. Bright Harbor Care Partners specializes in revenue cycle optimization, practice management improvement and developing new physician practices. Our technical skills allow us to dig deep into your revenue cycle while our strategic approach ensures we're keeping our eyes on the entire financial picture. By implementing a comprehensive approach to optimization and working closely with your people, processes, and technology, we develop a complete picture of your organization's performance. More importantly, we're able to design strategies and solutions that improve this performance while also preserving your organization's mission, vision, and strategic initiatives.</p>
  </div>

  <div class="abs pillars">
    <div class="pillar">
      <div class="pillar__icon"><svg width="24" height="24" viewBox="0 0 24 24" fill="none" stroke="var(--blue)" stroke-width="2"><path d="M3 9l9-5 9 5-9 5z"/><path d="M7 12v5h10v-5"/></svg></div>
      <div class="pillar__label">CONVEY KNOWLEDGE</div>
    </div>
    <div class="pillar">
      <div class="pillar__icon"><svg width="24" height="24" viewBox="0 0 24 24" fill="var(--blue)"><circle cx="12" cy="7" r="4"/><path d="M5 19c0-4 3-6 7-6s7 2 7 6z"/></svg></div>
      <div class="pillar__label">EXPERTISE</div>
    </div>
    <div class="pillar">
      <div class="pillar__icon"><svg width="24" height="24" viewBox="0 0 24 24" fill="none" stroke="var(--blue)" stroke-width="2"><path d="M3 12l5-4 4 3 4-3 5 4-7 6z"/></svg></div>
      <div class="pillar__label">PARTNERSHIP AND<br>STRENGTH</div>
    </div>
  </div>

  <div class="abs services">
    <h2 class="section-title" style="color:var(--sky-light);margin-bottom:16px">SERVICE</h2>
    <div class="service">
      <svg class="service__icon" viewBox="0 0 28 28" fill="none" stroke="#fff" stroke-width="3"><path d="M22 9a10 10 0 1 0 2 7"/><path d="M24 4v6h-6"/></svg>
      <div class="service__name">REVENUE CYCLE OPTIMIZATION</div>
      <div class="service__sub">(Making my clients money)</div>
      <p class="body-text">In today's increasingly complex health care environment it's important now more than ever that medical practices closely manage their revenue cycle. Bright Harbor Care Partners (BHC) understands the reimbursement landscape</p>
    </div>
    <div class="service">
      <svg class="service__icon" viewBox="0 0 28 28" fill="none" stroke="#fff" stroke-width="2.4"><circle cx="14" cy="9" r="5"/><path d="M3 16v6l6 3h8l7-5"/></svg>
      <div class="service__name">PRACTICE MANAGEMENT OPTIMIZATION</div>
      <div class="service__sub">(Improving clinical operations)</div>
      <p class="body-text">Practice Management is challenging and it requires the right balance of skill, knowledge, experience and management expertise. BHC Offers assessment and optimization in Patient Access &amp; Scheduling, Patient Experience, Staff Experience</p>
    </div>
    <div class="service">
      <svg class="service__icon" viewBox="0 0 28 28" fill="none" stroke="#fff" stroke-width="2.4"><rect x="5" y="3" width="18" height="22" rx="2"/><path d="M9 12h10M9 17h10"/></svg>
      <div class="service__name">HEALTH COMPLIANCE</div>
      <div class="service__sub">(Following the law)</div>
      <p class="body-text">Bright Harbor Care Partners (BHC) is a healthcare consulting firm skilled at helping physician practices advance their strategic vision in an ever-evolving healthcare system. Bright Harbor Care Partners specializes in revenue cycle optimization, practice management improvement and developing new physician practices.</p>
    </div>
    <div class="service">
      <svg class="service__icon" viewBox="0 0 28 28" fill="none" stroke="#fff" stroke-width="2.4"><rect x="7" y="3" width="16" height="18" rx="2"/><path d="M3 24h22M11 9h8M11 14h8"/></svg>
      <div class="service__name">HEALTH CARE TECHNOLOGY</div>
      <div class="service__sub">(Telemedicine and AI)</div>
      <p class="body-text">Our technical skills allow us to dig deep into your revenue cycle while our strategic approach ensures we're keeping our eyes on the entire financial picture. By implementing a comprehensive approach to optimization and working closely with your people, processes, and technology, we develop a complete picture of your organization's performance.</p>
    </div>
  </div>

  <svg class="abs corner-wave" style="left:0;top:830px" width="331" height="56" viewBox="0 0 331 56"><path d="M0 0 Q10 50 60 56 L0 56Z" fill="var(--sky)"/></svg>

  <footer class="abs footer">
    <div class="abs call"><span class="call__label">CALL US NOW:</span><span class="call__phone">(555) 014-2870</span></div>
    <div class="abs contact">
      <div class="contact__row"><svg width="13" height="13" viewBox="0 0 14 14" fill="none" stroke="#fff" stroke-width="1.4"><circle cx="7" cy="7" r="6"/><path d="M1 7h12M7 1c3 3 3 9 0 12M7 1c-3 3-3 9 0 12"/></svg>www.brightharborcare.net</div>
      <div class="contact__row"><svg width="13" height="11" viewBox="0 0 14 11" fill="none" stroke="#fff" stroke-width="1.4"><rect x="1" y="1" width="12" height="9"/><path d="M1 1l6 5 6-5"/></svg>info@brightharborcare.net</div>
    </div>
  </footer>
</section>

<!-- BACK -->
<section class="page page--back">
  <div class="photo desk-photo" role="img" aria-label="Business meeting with hands signing a document on a clipboard over a desk"></div>
  <svg class="abs" style="left:0;top:346px" width="330" height="40" viewBox="0 0 330 40"><path d="M0 40 Q0 0 40 0 L330 0 L330 40Z" fill="#fff"/></svg>

  <div class="abs expertise-panel">
    <div class="abs expertise">
      <h2 class="section-title" style="color:var(--sky-light)">EXPERTISE</h2>
      <div class="expertise__sub">People Make All The Difference</div>
      <p class="body-text">The varied expertise of our team encompass full service revenue cycle management, practice management, regulatory compliance, human resource management, and full spectrum health care consulting services. The teams coming together to support our clients include specialists with designations and degrees ranging from:</p>
      <ul class="checks">
        <li><svg width="13" height="13" viewBox="0 0 14 14" fill="none" stroke="#fff" stroke-width="1.4"><circle cx="7" cy="7" r="6"/><path d="M4 7l2 2 5-5"/></svg>Certified Health Care Financial Professional (CHFP)</li>
        <li><svg width="13" height="13" viewBox="0 0 14 14" fill="none" stroke="#fff" stroke-width="1.4"><circle cx="7" cy="7" r="6"/><path d="M4 7l2 2 5-5"/></svg>Certified Revenue Cycle Specialist (CRCR)</li>
        <li><svg width="13" height="13" viewBox="0 0 14 14" fill="none" stroke="#fff" stroke-width="1.4"><circle cx="7" cy="7" r="6"/><path d="M4 7l2 2 5-5"/></svg>Certified Medical Reimbursement Specialist (CMRS)</li>
        <li><svg width="13" height="13" viewBox="0 0 14 14" fill="none" stroke="#fff" stroke-width="1.4"><circle cx="7" cy="7" r="6"/><path d="M4 7l2 2 5-5"/></svg>Certified Professional Coder (CPC)</li>
        <li><svg width="13" height="13" viewBox="0 0 14 14" fill="none" stroke="#fff" stroke-width="1.4"><circle cx="7" cy="7" r="6"/><path d="M4 7l2 2 5-5"/></svg>Certified Specialist Physician Practice Management (CSPPM)</li>
        <li><svg width="13" height="13" viewBox="0 0 14 14" fill="none" stroke="#fff" stroke-width="1.4"><circle cx="7" cy="7" r="6"/><path d="M4 7l2 2 5-5"/></svg>Certified Medical Practice Executive (CMPE)</li>
        <li><svg width="13" height="13" viewBox="0 0 14 14" fill="none" stroke="#fff" stroke-width="1.4"><circle cx="7" cy="7" r="6"/><path d="M4 7l2 2 5-5"/></svg>Certified in HealthCare Compliance (CHC)</li>
      </ul>
    </div>
    <div class="photo team-photo" role="img" aria-label="Two consultants reviewing charts at a laptop in an office"></div>
  </div>

  <div class="abs left-col">
    <h2 class="section-title">CONVEY KNOWLEDGE</h2>
    <p class="body-text">Lorem Ipsum is simply dummy text of the printing and typesetting industry. Lorem Ipsum has been the industry's standard dummy text ever since the 1500s, when an unknown printer took a galley of type and scrambled it to make a type specimen book.Lorem Ipsum is simply dummy text of the printing and typesetting industry. Lorem Ipsum is simply dummy text of the printing and typesetting industry.</p>
    <h2 class="section-title" style="line-height:21px">PARTNERSHIP AND<br>STRENGTH</h2>
    <p class="body-text">Bright Harbor Care Partners (BHC) is a healthcare consulting firm skilled at helping physician practices advance their strategic vision in an ever-evolving healthcare system. Bright Harbor Care Partners specializes in revenue cycle optimization, practice management improvement and developing new physician practices. Our technical skills allow us to dig deep into your revenue cycle while our strategic approach ensures we're keeping our eyes on the entire financial picture</p>
  </div>
  <div class="abs map" role="img" aria-label="Street map showing the office location"></div>

  <svg class="abs" style="left:0;top:840px" width="331" height="58" viewBox="0 0 331 58"><path d="M0 0 Q10 52 60 58 L0 58Z" fill="var(--sky)"/></svg>

  <footer class="abs footer" style="top:898px;height:54px">
    <div class="abs address" style="top:15px"><svg width="14" height="18" viewBox="0 0 14 18" fill="none" stroke="#fff" stroke-width="1.6"><path d="M7 17C3 11 1 8 1 6a6 6 0 0 1 12 0c0 2-2 5-6 11z"/><circle cx="7" cy="6" r="2"/></svg>118 Harbor Lane, Portview, Ny 10099, Usa</div>
    <div class="abs web" style="top:16px"><svg width="13" height="13" viewBox="0 0 14 14" fill="none" stroke="#fff" stroke-width="1.4"><circle cx="7" cy="7" r="6"/><path d="M1 7h12M7 1c3 3 3 9 0 12M7 1c-3 3-3 9 0 12"/></svg>www.brightharborcare.net</div>
  </footer>
</section>

</body>
</html>
```